GSTP1 - 1 of 21 projects

We need info graphics to describe and explain the characteristics of a specific gene of the human genome called "GSTP1" for a illustrated report, and salable product.

The illustrated report needs to have a clean medical, and futuristic science feel.

We have words, and need to illustrate these concepts at a grade 8 level.
Updates

Successful design will trigger opportunity to all gene projects totaling 21 similar projects.

We are planning to decide on a design by Midnight tonight.

Target Market(s)

middle income and upper class,and executive, free world markets.

Industry/Entity Type

Medical

Requirements
Must have
• A clear illustrated description of the primary characteristics of GSTP1. GSTP1 is part of a network of enzymes which help eliminate the dangerous wastes in the human body protecting damage to cell membrane, DNA, and protein.
• Our customers will want to see this and understand illustrations.
Nice to have
• color - primary blue of multiple shades.

```html
<!DOCTYPE html>
<html lang="en">
<head>
<meta charset="utf-8">
<title>GSTP 1 – Detoxifier Types</title>
<link href="https://fonts.googleapis.com/css2?family=Open+Sans:wght@400;700&display=swap" rel="stylesheet">
<style>
  :root {
    --band-top: #16e3fb;
    --band-bottom: #0ab3e0;
    --accent-orange: #f7941d;
    --label-orange: #f9a03f;
    --stage-bg: #f2f2f2;
    --figure-light: #ffffff;
    --figure-edge: #e4e4e4;
    --text-white: #ffffff;
    --text-dark: #1a1a1a;
    --hazard-yellow: #f7d417;
    --hazard-ink: #1a1a1a;
    --capsule-lime: #c9e21a;
    --capsule-purple: #b23fcf;
    --pill-red: #e8323c;
    --pill-blue: #2f7fe0;
  }
  * { margin: 0; padding: 0; box-sizing: border-box; }
  html, body { width: 1200px; height: 1107px; overflow: hidden; }
  body {
    font-family: "Open Sans", Arial, sans-serif;
    background: var(--stage-bg);
    position: relative;
  }
  .header-band {
    position: absolute; left: 0; top: 0; width: 1200px; height: 132px;
    background: linear-gradient(180deg, var(--band-top), var(--band-bottom));
    border-bottom: 4px solid var(--accent-orange);
  }
  .title {
    position: absolute; left: 97px; top: 42px;
    color: var(--text-white); font-weight: 700; font-size: 39px; letter-spacing: 0.5px;
  }
  .stage {
    position: absolute; left: 0; top: 136px; width: 1200px; height: 854px;
    background:
      repeating-linear-gradient(0deg, rgba(0,0,0,0.012) 0 2px, transparent 2px 6px),
      var(--stage-bg);
  }
  .figure {
    position: absolute; top: 30px; height: 824px;
    background: radial-gradient(ellipse at 50% 45%, var(--figure-light) 60%, var(--figure-edge) 100%);
    border-radius: 140px 140px 30px 30px;
  }
  .figure-good { left: 97px; width: 300px; }
  .figure-average { left: 502px; width: 280px; }
  .figure-poor { left: 895px; width: 292px; }
  .markers {
    position: absolute; left: 0; top: 0; width: 1200px; height: 1107px;
    pointer-events: none;
  }
  .hazard-shape { fill: var(--hazard-yellow); stroke: var(--hazard-ink); stroke-width: 2; stroke-linejoin: round; }
  .hazard-mark { fill: var(--hazard-ink); }
  .capsule-top { fill: var(--capsule-lime); }
  .capsule-bottom { fill: var(--capsule-purple); }
  .footer-band {
    position: absolute; left: 0; top: 990px; width: 1200px; height: 117px;
    background: linear-gradient(180deg, var(--band-bottom), var(--band-top));
    border-top: 4px solid var(--accent-orange);
  }
  .label {
    position: absolute; top: 3px; height: 69px;
    background: var(--label-orange);
    color: var(--text-dark); font-size: 27px;
    display: flex; align-items: center; justify-content: center;
  }
  .label::before {
    content: ""; position: absolute; top: -14px; left: 50%; margin-left: -14px;
    border-left: 14px solid transparent; border-right: 14px solid transparent;
    border-bottom: 14px solid var(--accent-orange);
  }
  .label-good { left: 110px; width: 270px; }
  .label-average { left: 500px; width: 300px; }
  .label-poor { left: 873px; width: 287px; }
</style>
</head>
<body>
  <header class="header-band">
    <h1 class="title">GSTP 1</h1>
  </header>

  <main class="stage">
    <div class="figure figure-good" role="img" aria-label="Human body outline, good detoxifier"></div>
    <div class="figure figure-average" role="img" aria-label="Human body outline, average detoxifier"></div>
    <div class="figure figure-poor" role="img" aria-label="Human body outline, poor detoxifier"></div>
  </main>

  <svg class="markers" viewBox="0 0 1200 1107" aria-hidden="false">
    <defs>
      <g id="hazard">
        <path class="hazard-shape" d="M0 -16 L18 15 L-18 15 Z"/>
        <rect class="hazard-mark" x="-2" y="-7" width="4" height="12" rx="1.5"/>
        <circle class="hazard-mark" cx="0" cy="9.5" r="2.3"/>
      </g>
      <g id="capsule">
        <path class="capsule-top" d="M-9 0 V-15 A9 9 0 0 1 9 -15 V0 Z"/>
        <path class="capsule-bottom" d="M-9 0 V15 A9 9 0 0 0 9 15 V0 Z"/>
      </g>
      <radialGradient id="pill-pile" cx="50%" cy="50%" r="60%">
        <stop offset="0%" stop-color="var(--pill-blue)"/>
        <stop offset="55%" stop-color="#5a6fd0"/>
        <stop offset="100%" stop-color="var(--pill-red)"/>
      </radialGradient>
    </defs>

    <g class="markers-good">
      <use href="#hazard" x="192" y="845"/>
      <use href="#hazard" x="300" y="845"/>
      <use href="#capsule" x="196" y="900"/>
      <use href="#capsule" x="300" y="894"/>
    </g>

    <g class="markers-average">
      <ellipse cx="638" cy="540" rx="56" ry="34" fill="url(#pill-pile)" role="img" aria-label="Heap of red and blue pills at the hips"/>
      <use href="#hazard" x="584" y="666"/>
      <use href="#hazard" x="688" y="663"/>
      <use href="#capsule" x="586" y="780"/>
      <use href="#capsule" x="690" y="773"/>
      <use href="#hazard" x="584" y="845"/>
      <use href="#hazard" x="688" y="843"/>
    </g>

    <g class="markers-poor">
      <use href="#hazard" x="1029" y="220"/>
      <ellipse cx="1025" cy="350" rx="56" ry="34" fill="url(#pill-pile)" role="img" aria-label="Heap of red and blue pills in the chest"/>
      <use href="#hazard" x="1029" y="446"/>
      <use href="#capsule" x="914" y="467"/>
      <use href="#capsule" x="1143" y="464"/>
      <ellipse cx="1028" cy="548" rx="56" ry="34" fill="url(#pill-pile)" role="img" aria-label="Heap of red and blue pills at the hips"/>
      <use href="#hazard" x="975" y="666"/>
      <use href="#hazard" x="1080" y="663"/>
      <use href="#capsule" x="978" y="747"/>
      <use href="#capsule" x="1082" y="740"/>
      <use href="#hazard" x="975" y="815"/>
      <use href="#hazard" x="1080" y="812"/>
    </g>
  </svg>

  <footer class="footer-band">
    <div class="label label-good">Good Detoxifier</div>
    <div class="label label-average">Average Detoxifier</div>
    <div class="label label-poor">Poor Detoxifier</div>
  </footer>
</body>
</html>
```